Content processing platform needs a landing page for products

We need a general landing page for products that we are launching. The concept of the product page is to do two things: a) Get users to sign up for our waitlist (que) so they get access to the product (we give access weekly). b) To generate interest for future products that we have not decided on yet. Mockups: Please see our mockups for inspiration. You have pretty free hands to combine, but please don't let our users think :-). Style: Please use the colours of our style sheet and see the home page (plintrel.com) for inspiration on how we want the style and tone to be. The final design should communicate "scaling".

Target Market(s)

B2B - online businesses big and small that wish to scale their production of content and translation.

Industry/Entity Type

SaaS

Number of Pages Required

1 page

Font styles to use
Other font styles liked:
• open sans

Requirements
Must have
• Follow our styleguide.

```html
<!DOCTYPE html>
<html lang="en">
<head>
<meta charset="utf-8">
<title>Plintrel – Soon Available</title>
<link href="https://fonts.googleapis.com/css2?family=Open+Sans:wght@300;400;600;700&display=swap" rel="stylesheet">
<style>
  :root {
    --ink: #222222;
    --black: #000000;
    --white: #ffffff;
    --pink: #f0386b;
    --blue: #12a3e3;
    --muted: #4a4a4a;
    --body: #5a5a5a;
    --footer-link: #b8b8b8;
    --field-dark: #333333;
  }
  * { box-sizing: border-box; margin: 0; padding: 0; }
  html, body { width: 800px; height: 1200px; overflow: hidden; background: var(--white); }
  body { font-family: "Open Sans", Arial, sans-serif; color: var(--ink); }
  .page { position: relative; width: 800px; height: 1200px; overflow: hidden; }
  .backdrop { position: absolute; inset: 0; width: 800px; height: 1200px; }
  .abs { position: absolute; }

  .brand { left: 100px; top: 24px; font-size: 15px; font-weight: 700; color: var(--ink); letter-spacing: .3px; }
  .nav { left: 263px; top: 24px; display: flex; gap: 0; font-size: 15px; font-weight: 600; }
  .nav a { text-decoration: none; color: var(--ink); margin-right: 24px; }
  .nav a.active { color: var(--pink); }

  .product-shot { left: 132px; top: 112px; width: 190px; height: 304px;
    background: linear-gradient(180deg, #3a3a3a 0%, #1a1a1a 55%, #000 100%); border-radius: 4px; }

  .hero-title { left: 400px; width: 285px; top: 122px; text-align: center; font-size: 24px; font-weight: 600; letter-spacing: .5px; }
  .hero-sub { left: 400px; width: 285px; top: 186px; text-align: center; font-size: 12px; }
  .hero-sub strong { font-weight: 600; }
  .email-field { left: 433px; top: 214px; width: 219px; height: 30px; border: 2px solid var(--pink);
    display: flex; align-items: center; justify-content: center; font-size: 11.5px; color: #b5b5b5; background: var(--white); }
  .btn { display: flex; align-items: center; justify-content: center; background: var(--pink); color: var(--white);
    font-weight: 700; border-radius: 14px; }
  .hero-btn { left: 510px; top: 258px; width: 66px; height: 29px; font-size: 12px; box-shadow: 0 3px 6px rgba(0,0,0,.18); }

  .feature-label { top: 561px; width: 200px; text-align: center; font-size: 11.5px; font-weight: 700; color: var(--muted); }

  .section-title { left: 0; width: 766px; top: 754px; text-align: center; font-size: 14.5px; font-weight: 700; }

  .review { width: 185px; height: 228px; background: var(--white); border-radius: 9px;
    box-shadow: 0 4px 10px rgba(0,0,0,.15); text-align: center; }
  .avatar { width: 58px; height: 58px; border-radius: 50%; margin: 14px auto 0;
    background: radial-gradient(circle at 50% 40%, #c9a184, #7a5a48); }
  .review-name { margin-top: 14px; font-size: 12px; font-weight: 600; }
  .review-meta { font-size: 6.5px; color: var(--body); margin-top: 2px; }
  .review-text { margin: 26px 0 0 14px; width: 168px; text-align: left; font-size: 8.6px; font-weight: 300;
    line-height: 10.8px; color: var(--body); }

  .footer-links { left: 103px; top: 1133px; list-style: none; font-size: 7.5px; font-weight: 700; line-height: 17px; color: var(--footer-link); }
  .footer-links li:first-child { color: var(--pink); }
  .newsletter-label { left: 515px; top: 1149px; font-size: 8px; font-weight: 600; color: #555; letter-spacing: .3px; }
  .newsletter-field { left: 530px; top: 1168px; width: 105px; height: 16px; background: var(--field-dark);
    font-size: 8px; color: #8a8a8a; display: flex; align-items: center; justify-content: center; }
  .newsletter-btn { left: 647px; top: 1167px; width: 52px; height: 21px; font-size: 8.5px; border-radius: 11px; }
</style>
</head>
<body>
<div class="page">
  <svg class="backdrop" viewBox="0 0 1000 1500" preserveAspectRatio="none" aria-hidden="true">
    <rect width="1000" height="1500" fill="var(--black)"/>
    <polygon points="0,0 1000,0 1000,650 0,145" fill="var(--white)"/>
    <polygon points="0,655 1000,1090 1000,1420 0,980" fill="var(--white)"/>
  </svg>

  <div class="abs brand">plintrel</div>
  <nav class="abs nav">
    <a class="active" href="#">PRODUCTS</a>
    <a href="#">APPS</a>
    <a href="#">BLOG</a>
    <a href="#">HELP</a>
  </nav>

  <div class="abs product-shot" role="img" aria-label="Black pump bottle and its box, product photo"></div>

  <h1 class="abs hero-title">SOON AVAILABLE</h1>
  <p class="abs hero-sub"><strong>SIGN UP</strong> to be the first in line</p>
  <div class="abs email-field">Email</div>
  <div class="abs btn hero-btn">SIGN UP</div>

  <svg class="abs" style="left:96px;top:218px" width="16" height="24" viewBox="0 0 16 24" aria-hidden="true">
    <polyline points="12,3 4,12 12,21" fill="none" stroke="#a0163d" stroke-width="1.4"/>
  </svg>
  <svg class="abs" style="left:688px;top:218px" width="16" height="24" viewBox="0 0 16 24" aria-hidden="true">
    <polyline points="4,3 12,12 4,21" fill="none" stroke="#8a8a8a" stroke-width="1.4"/>
  </svg>

  <svg class="abs" style="left:372px;top:426px" width="50" height="8" viewBox="0 0 50 8" aria-hidden="true">
    <circle cx="7" cy="4" r="3" fill="var(--pink)"/>
    <circle cx="18" cy="4" r="3" fill="#777"/>
    <circle cx="30" cy="4" r="3" fill="#777"/>
    <circle cx="41" cy="4" r="3" fill="#777"/>
  </svg>

  <!-- Feature icons -->
  <svg class="abs" style="left:171px;top:507px" width="46" height="46" viewBox="0 0 46 46" aria-hidden="true">
    <g fill="none" stroke="var(--blue)" stroke-width="1.8">
      <circle cx="23" cy="23" r="20" stroke-dasharray="5 2"/>
      <circle cx="23" cy="23" r="15"/>
      <polygon points="23,14 25.6,20 32,20.4 27,24.6 28.6,31 23,27.4 17.4,31 19,24.6 14,20.4 20.4,20" stroke-linejoin="round"/>
    </g>
  </svg>
  <svg class="abs" style="left:368px;top:507px" width="44" height="44" viewBox="0 0 44 44" aria-hidden="true">
    <g fill="none" stroke="var(--blue)" stroke-width="1.8" stroke-linejoin="round" stroke-linecap="round">
      <path d="M6 22 L14 8 L24 6 L30 10 L38 14 L40 24 L32 36 L22 40 L12 36 Z"/>
      <path d="M14 14 L26 24 M18 10 L30 20 M20 30 L28 22 M12 26 L22 18"/>
    </g>
  </svg>
  <svg class="abs" style="left:578px;top:509px" width="52" height="42" viewBox="0 0 52 42" aria-hidden="true">
    <g fill="none" stroke="var(--blue)" stroke-width="1.8" stroke-linejoin="round">
      <rect x="2" y="3" width="30" height="28" rx="2"/>
      <path d="M32 12 H42 L49 22 V31 H32"/>
      <circle cx="17" cy="16" r="8"/>
      <polyline points="17,11 17,16 21,18"/>
      <circle cx="12" cy="34" r="4" fill="var(--white)"/>
      <circle cx="40" cy="34" r="4" fill="var(--white)"/>
    </g>
  </svg>
  <div class="abs feature-label" style="left:94px">BEST QUALITY</div>
  <div class="abs feature-label" style="left:290px">CUSTOMERS TRUST US</div>
  <div class="abs feature-label" style="left:503px">FAST DELIVERY</div>

  <h2 class="abs section-title">WHAT OUR CUSTOMERS SAY ABOUT US</h2>

  <article class="abs review" style="left:98px;top:804px">
    <div class="avatar" role="img" aria-label="Portrait photo of a smiling customer"></div>
    <div class="review-name">Dana Merrow</div>
    <div class="review-meta">24, USA</div>
    <p class="review-text">Lorem ipsum dolor sit amet, consectetur adipiscing elit, sed do eiusmod tempor incididunt ut labore et dolore magna aliqua. Ut enim ad minim veniam, quis nostrud exercitation ullamco laboris nisi ut aliquip ex ea commodo consequat.</p>
  </article>
  <article class="abs review" style="left:304px;top:803px">
    <div class="avatar" role="img" aria-label="Portrait photo of a customer"></div>
    <div class="review-name">Dana Merrow</div>
    <div class="review-meta">24, USA</div>
    <p class="review-text">Lorem ipsum dolor sit amet, consectetur adipiscing elit, sed do eiusmod tempor incididunt ut labore et dolore magna aliqua. Ut enim ad minim veniam, quis nostrud exercitation ullamco laboris nisi ut aliquip ex ea commodo consequat.</p>
  </article>
  <article class="abs review" style="left:514px;top:805px">
    <div class="avatar" role="img" aria-label="Portrait photo of a customer"></div>
    <div class="review-name">Dana Merrow</div>
    <div class="review-meta">24, USA</div>
    <p class="review-text">Lorem ipsum dolor sit amet, consectetur adipiscing elit, sed do eiusmod tempor incididunt ut labore et dolore magna aliqua. Ut enim ad minim veniam, quis nostrud exercitation ullamco laboris nisi ut aliquip ex ea commodo consequat.</p>
  </article>

  <svg class="abs" style="left:0;top:0" width="800" height="1200" viewBox="0 0 800 1200" aria-hidden="true" pointer-events="none">
    <g stroke="var(--blue)" stroke-width="1.6" fill="var(--blue)">
      <line x1="265" y1="818" x2="314" y2="818"/>
      <line x1="480" y1="818" x2="529" y2="818"/>
      <line x1="265" y1="1013" x2="314" y2="1013"/>
      <line x1="480" y1="1013" x2="529" y2="1013"/>
      <circle cx="265" cy="818" r="5" stroke="none"/><circle cx="314" cy="818" r="5" stroke="none"/>
      <circle cx="480" cy="818" r="5" stroke="none"/><circle cx="529" cy="818" r="5" stroke="none"/>
      <circle cx="265" cy="1013" r="5" stroke="none"/><circle cx="314" cy="1013" r="5" stroke="none"/>
      <circle cx="480" cy="1013" r="5" stroke="none"/><circle cx="529" cy="1013" r="5" stroke="none"/>
    </g>
  </svg>

  <ul class="abs footer-links">
    <li>Products</li>
    <li>Quality check</li>
    <li>Reviews</li>
    <li>Help</li>
  </ul>
  <div class="abs newsletter-label">SIGN UP TO OUR NEWSLETTER</div>
  <div class="abs newsletter-field">Email</div>
  <div class="abs btn newsletter-btn">SIGN UP</div>
</div>
</body>
</html>
```